Tidewell Care Group Site Re-Design

Review content of current website www.tidewellcaregroup.example and re-design each page - I have attached a comprehensive website brief which outlines the products and services that tidewell care group sells online, the type of style I like my website to be in which is clean, uncluttered, professional and modern, it also indicates which other websites that I admire and that I would like my existing site to be changed to that style. The Personal Trainer Development Sub Page is going to be re -written and I am hoping that the new design will make my site more modern and provide a better user experience. I would also be open if the designer wanted to use their creative talents to re-design my logo if you think you could do a better job. I look forward to seeing some awesome designs.

Target Market(s)

Refer to attached design brief

Industry/Entity Type

Health And Wellness

Number of Pages Required

5+ page

Colors
9bcb3c
6b449b

Requirements
Must have
• Refer to design brief
Nice to have
• Refer to design brief
Should not have
• Refer to design brief

```html
<!DOCTYPE html>
<html lang="en">
<head>
<meta charset="utf-8">
<title>Tidewell Care Group</title>
<link href="https://fonts.googleapis.com/css2?family=Open+Sans:ital,wght@0,300;0,400;0,600;0,700;0,800;1,300;1,400&display=swap" rel="stylesheet">
<style>
:root{
  --green:#9bcb3c;
  --purple:#6b449b;
  --heading:#6b6b6b;
  --text:#7a7a7a;
  --light-bg:#f3f3ef;
  --white:#ffffff;
}
*{margin:0;padding:0;box-sizing:border-box}
html,body{width:1200px;height:5091px;overflow:hidden}
body{position:relative;font-family:"Open Sans",Arial,sans-serif;color:var(--text);background:var(--white)}
.abs{position:absolute}
.photo{position:absolute}

/* header */
.site-header{position:absolute;left:0;top:0;width:1200px;height:119px;background:var(--white);border-bottom:4px solid var(--green)}
.brand{position:absolute;left:99px;top:44px;display:flex;align-items:center;gap:10px;font-weight:700;font-size:17px;color:var(--purple)}
.brand-dot{width:22px;height:22px;border-radius:50%;background:var(--green)}
.main-nav{position:absolute;right:99px;top:52px;display:flex;gap:30px;font-size:13px;color:#8a8a8a}
.main-nav .active{color:var(--green)}

/* hero */
.hero{left:0;top:123px;width:1200px;height:648px;background:linear-gradient(180deg,#2f4a26 0%,#4e6b3a 45%,#6c6a5e 75%,#8a877c 100%)}
.hero-title{left:99px;top:276px;color:var(--white);font-size:62px;line-height:60px;text-transform:uppercase}
.hero-title b{font-weight:800;display:block}
.hero-title span{font-weight:300;display:block}
.hero-copy{left:99px;top:410px;width:400px;color:var(--white);font-size:12.5px;line-height:20px}
.btn{background:var(--green);color:var(--white);font-weight:600;display:flex;align-items:center;justify-content:center}
.hero-btn{left:99px;top:546px;width:171px;height:42px;font-size:16px;font-weight:700}
.slider-arrow{color:rgba(255,255,255,.6);font-size:36px;font-weight:300}

/* section titles */
.section-title{left:0;width:1200px;text-align:center;font-weight:700;font-size:38px;color:var(--heading)}

/* service cards */
.service-card{top:949px;width:314px;height:500px;background:var(--white);box-shadow:0 1px 5px rgba(0,0,0,.18)}
.service-card .photo{left:0;top:0;width:314px;height:254px}
.service-card h3{position:absolute;left:24px;top:280px;width:270px;font-weight:400;font-size:18px;line-height:22px;color:var(--purple);text-transform:uppercase}
.service-card p{position:absolute;left:24px;top:342px;width:270px;font-size:12px;line-height:20px}
.service-card .btn{position:absolute;left:24px;top:428px;width:140px;height:36px;font-size:14px;font-weight:400}

/* contact */
.contact{left:0;top:1546px;width:1200px;height:981px;background:linear-gradient(135deg,#6a4a9e 0%,#5a4a9c 55%,#4f4f9f 100%)}
.contact h2{position:absolute;left:0;top:52px;width:1200px;text-align:center;color:var(--white);font-size:38px;font-weight:700}
.contact .lead{position:absolute;left:0;top:123px;width:1200px;text-align:center;color:var(--white);font-size:12px}
.trial-card{left:372px;top:1726px;width:454px;height:666px;background:var(--white)}
.trial-card .photo{left:0;top:0;width:454px;height:304px}
.trial-card h3{position:absolute;left:38px;top:322px;font-size:26px;font-weight:700;color:var(--purple)}
.trial-card .note{position:absolute;left:38px;top:366px;width:360px;font-size:12px;line-height:20px;color:#8a8a8a}
.field{position:absolute;left:38px;width:374px}
.field label{display:block;font-size:12px;color:var(--purple);margin-bottom:6px}
.field span{display:block;height:30px;border:1px solid #cfcfcf}
.submit{left:662px;top:2343px;width:122px;height:122px;border-radius:50%;background:var(--green);color:var(--white);font-weight:700;font-size:20px;display:flex;align-items:center;justify-content:center}

/* testimonials */
.quote{left:185px;top:2686px;width:830px;text-align:center;font-style:italic;font-weight:300;font-size:19px;line-height:29px;color:#666}
.quote-mark{font-size:90px;color:#e4e4e4;font-family:Georgia,serif;line-height:1}
.avatar-ring{left:530px;top:2847px;width:142px;height:142px;border-radius:50%;background:var(--white);box-shadow:0 0 6px rgba(0,0,0,.15)}
.avatar{left:538px;top:2855px;width:126px;height:126px;border-radius:50%;background:radial-gradient(circle,#c99f7c 0%,#8a6b52 70%,#5f4a3c 100%)}
.client-name{left:0;top:3008px;width:1200px;text-align:center;font-size:16px;letter-spacing:1px;color:#555}

/* video */
.video-band{left:0;top:3120px;width:1200px;height:840px;background:var(--light-bg)}
.video-frame{left:99px;top:3276px;width:1000px;height:433px;background:var(--white);box-shadow:0 1px 4px rgba(0,0,0,.12)}
.video-frame .photo{left:10px;top:10px;width:980px;height:413px;background:linear-gradient(90deg,#c7c2bb 0%,#d9d4cf 45%,#bfb6ad 100%)}
.video-copy{left:185px;top:3748px;width:830px;text-align:center;font-size:12.5px;line-height:26px;color:#6f6f6f}

/* blog */
.blog-card{top:4108px;width:316px}
.blog-card .photo{left:0;top:0;width:316px;height:183px}
.blog-date{position:absolute;right:0;top:0;background:var(--white);padding:4px 14px;font-size:12px;color:var(--purple)}
.blog-card h3{position:absolute;left:4px;top:214px;width:310px;font-weight:400;font-size:17px;line-height:21px;color:var(--purple);text-transform:uppercase}
.blog-card p{position:absolute;left:4px;top:272px;width:310px;font-size:12px;line-height:21px}
.blog-card .btn{position:absolute;left:4px;top:360px;width:126px;height:38px;font-size:15px;font-weight:400}

/* footer */
.site-footer{left:0;top:4612px;width:1200px;height:479px;background:var(--green);color:var(--white);text-align:center}
.top-badge{left:577px;top:4589px;width:46px;height:46px;border-radius:50%;background:var(--white);color:var(--green);font-size:9px;font-weight:700;display:flex;align-items:flex-end;justify-content:center;padding-bottom:8px}
.footer-nav{position:absolute;left:0;top:92px;width:1200px;display:flex;justify-content:center;font-size:9.5px}
.footer-nav span{padding:0 9px;border-left:1px solid rgba(255,255,255,.7)}
.footer-nav span:first-child{border-left:none}
.site-footer h2{position:absolute;left:0;top:158px;width:1200px;font-size:26px;font-weight:400}
.site-footer .sub{position:absolute;left:0;top:203px;width:1200px;font-size:11px}
.signup{position:absolute;left:522px;top:245px;width:154px;height:50px;border:2px solid var(--white);font-size:20px;font-weight:600;display:flex;align-items:center;justify-content:center}
.socials{position:absolute;left:0;top:328px;width:1200px;display:flex;justify-content:center;gap:12px}
.socials i{width:30px;height:30px;border-radius:50%;background:var(--white);display:block}
.copyright{position:absolute;left:0;top:432px;width:1200px;font-size:10.5px}
</style>
</head>
<body>

<header class="site-header">
  <div class="brand"><span class="brand-dot"></span>Tidewell Care Group</div>
  <nav class="main-nav">
    <span class="active">Home</span><span>About</span><span>Contact</span><span>Services</span><span>Testimonials</span><span>Products</span><span>90 Day Challenge</span><span>Tidewell Life Blog</span>
  </nav>
</header>

<section>
  <div class="photo hero" role="img" aria-label="Woman in a yoga lunge pose on a rocky forest path surrounded by palms"></div>
  <span class="abs slider-arrow" style="left:36px;top:400px">‹</span>
  <span class="abs slider-arrow" style="left:1146px;top:400px">›</span>
  <h1 class="abs hero-title"><b>Tidewell</b><span>Care Group</span></h1>
  <p class="abs hero-copy">To provide you with the knowledge, information, qualifications and tools so that you can make well-informed decisions regarding your health &amp; fitness and transfer that knowledge to others for their health and well being.</p>
  <div class="abs btn hero-btn">LEARN MORE &gt;&gt;</div>
</section>

<h2 class="abs section-title" style="top:836px">Our Services</h2>

<article class="abs service-card" style="left:99px">
  <div class="photo" role="img" aria-label="Trainer spotting a client lifting dumbbells in a gym" style="background:linear-gradient(135deg,#9aa8b8,#4c5560)"></div>
  <h3>Fitness Courses and Education</h3>
  <p>Tidewell Care Group can provide you with not only the best fitness courses but will also provide a clear pathway to work experience.</p>
  <div class="btn">Learn more</div>
</article>
<article class="abs service-card" style="left:443px">
  <div class="photo" role="img" aria-label="Woman in a stretching pose on rocks in a garden" style="background:linear-gradient(135deg,#3f6a32,#7c8a6c)"></div>
  <h3>Customized Nutrition and Training</h3>
  <p>Tidewell Care Group have a wide range of training programs ranging from Weight loss, Strength &amp; Toning through to General Fitness.</p>
  <div class="btn">Learn more</div>
</article>
<article class="abs service-card" style="left:785px">
  <div class="photo" role="img" aria-label="Woman pressing dumbbells on a bench in a gym with orange walls" style="background:linear-gradient(135deg,#d85a3a,#3d3d44)"></div>
  <h3>Personal Trainer Business Tools</h3>
  <p>TCG provides business development training courses for those already operating within the Health &amp; Fitness Industry.</p>
  <div class="btn">Learn more</div>
</article>

<section class="abs contact" role="img" aria-label="Purple tinted photo of a person training with a medicine ball">
  <h2>Contact Information</h2>
  <p class="lead">We welcome your enquiry and look forward to hearing from you soon. our friendly staff at Tidewell Care Group are waiting to assist you.</p>
</section>
<div class="abs trial-card">
  <div class="photo" role="img" aria-label="Woman meditating cross-legged on grass" style="background:linear-gradient(180deg,#6f8a4e,#93a86a)"></div>
  <h3>Free Trial</h3>
  <p class="note">Enter Your Details Below with your enquiry and we will be in touch within 24 hours.....</p>
  <div class="field" style="top:420px"><label>First Name</label><span></span></div>
  <div class="field" style="top:480px"><label>Last Name</label><span></span></div>
  <div class="field" style="top:540px"><label>Email</label><span></span></div>
</div>
<div class="abs submit">Submit</div>

<h2 class="abs section-title" style="top:2606px">Client Testimonials</h2>
<span class="abs slider-arrow" style="left:98px;top:2736px;color:#cfcfcf">‹</span>
<span class="abs slider-arrow" style="left:1082px;top:2736px;color:#cfcfcf">›</span>
<span class="abs quote-mark" style="left:140px;top:2672px">“</span>
<span class="abs quote-mark" style="left:1006px;top:2790px">”</span>
<p class="abs quote">But I must explain to you how all this mistaken idea of denouncing pleasure and praising pain was born and I will give you a complete account of the system, and expound the actual teachings of the great explorer of the truth, the master-builder of human happiness. No one rejects, dislikes, or avoids pleasure itself, because it is pleasure, but because those who do not know how to pursue pleasure rationally encounter consequences that are extremely painful</p>
<div class="abs avatar-ring"></div>
<div class="abs avatar" role="img" aria-label="Client portrait"></div>
<p class="abs client-name">- ASSUMENDA EST</p>

<section class="abs video-band"></section>
<h2 class="abs section-title" style="top:3182px">Our Video</h2>
<div class="abs video-frame">
  <div class="photo" role="img" aria-label="Group of five fitness trainers smiling in a gym"></div>
  <svg class="abs" style="left:465px;top:182px" width="70" height="70" viewBox="0 0 70 70">
    <circle cx="35" cy="35" r="33" fill="rgba(255,255,255,.75)"/>
    <path d="M27 20 L52 35 L27 50 Z" fill="#6b449b"/>
  </svg>
</div>
<p class="abs video-copy">At vero eos et accusamus et iusto odio dignissimos ducimus qui blanditiis praesentium voluptatum deleniti atque corrupti quos dolores et quas molestias excepturi sint occaecati cupiditate non provident, similique sunt in culpa qui officia deserunt mollitia animi, id est laborum et dolorum fuga. Et harum quidem rerum facilis est et expedita distinctio. Nam libero tempore, cum soluta nobis est eligendi optio cumque nihil impedit quo minus id quod maxime placeat facere possimus, omnis voluptas assumenda est, omnis dolor repellendus. Temporibus autem quibusdam et aut officiis debitis aut rerum necessitatibus saepe eveniet ut et voluptates repudiandae sint et molestiae non recusandae.</p>

<h2 class="abs section-title" style="top:4008px">Our Blog</h2>
<article class="abs blog-card" style="left:99px">
  <div class="photo" role="img" aria-label="Woman working out on a gym machine" style="background:linear-gradient(135deg,#4e463c,#b59a78)"></div>
  <span class="blog-date">03-May-2016</span>
  <h3>Healthy Nutrition to Boost Your Gains</h3>
  <p>The human body is the most amazing and efficient machine on the planet. Put simply you only get out what you put in and I am sure you have all heard.</p>
  <div class="btn">Read More ›</div>
</article>
<article class="abs blog-card" style="left:442px">
  <div class="photo" role="img" aria-label="Two women training with a yellow exercise ball on blue mats" style="background:linear-gradient(135deg,#c49a52,#2f6ea8)"></div>
  <span class="blog-date">03-May-2016</span>
  <h3>Average of 30 Grams Protein Shake of Your Choice</h3>
  <p>If you can successfully incorporate healthy nutrition into your daily regime and combine this with a regular exercise program.</p>
  <div class="btn">Read More ›</div>
</article>
<article class="abs blog-card" style="left:786px">
  <div class="photo" role="img" aria-label="Woman lifting a kettlebell in a gym" style="background:linear-gradient(135deg,#6c7a8c,#c9bfb4)"></div>
  <span class="blog-date">03-May-2016</span>
  <h3>The Best Green Smoothie to Start Your Day</h3>
  <p>The King of Green Smoothies would have to be my Superfood Green Smoothie which contains all the elements necessary for unbelievable muscle.</p>
  <div class="btn">Read More ›</div>
</article>

<footer class="abs site-footer">
  <nav class="footer-nav">
    <span>HOME</span><span>ABOUT</span><span>CONTACT</span><span>SERVICES</span><span>TESTIMONIALS</span><span>PRODUCTS</span><span>90 DAY CHALLENGE</span><span>TIDEWELL LIFE BLOG</span>
  </nav>
  <h2>SUBSCRIBE YOUR NEWSLETTER</h2>
  <p class="sub">sign up with your email address to receive news and updates</p>
  <div class="signup">SIGN UP</div>
  <div class="socials"><i></i><i></i><i></i><i></i><i></i></div>
  <p class="copyright">© 2017 TIDEWELL CARE GROUP . ALL RIGHTS RESERVED.</p>
</footer>
<div class="abs top-badge">TOP</div>

</body>
</html>
```